Elegant Black Candle Label Design!

I need a 2.375" tall by 3.0" wide candle label design. I'm looking for simple and elegant. Black label with silver leaf border and lettering. Label needs to have the following information on it: Fern Hollow Candle Co. as the company name, scent name in the middle and in smaller font, it needs to say Made in USA, All Natural, 8oz. Attached photos are for inspiration.

Target Market(s)

People looking for high end, all natural candle fragrances

Industry/Entity Type

Candle-Spa

Colors

Designer to choose only greyscale colors for use in the design.

Requirements
Must have
• Company Name, Scent (ability to change scent names), All Natural, Made in USA, 8oz
Nice to have
• Black background, silver leaf border and silver leaf font. Elegant fonts maybe slightly cursive

```html
<!DOCTYPE html>
<html lang="en">
<head>
<meta charset="utf-8">
<title>Fern Hollow Candle Co. – Soy Candle Label</title>
<link rel="stylesheet" href="https://fonts.googleapis.com/css2?family=Great+Vibes&family=Uncial+Antiqua&family=Poppins:wght@400&display=swap">
<style>
  :root {
    --label-black: #050708;
    --silver-light: #d9d9d9;
    --silver-mid: #8c8c8c;
    --silver-dark: #3c3c3c;
    --text-silver: #cfcfcf;
    --brand-bronze: #9a6a52;
  }
  * { margin: 0; padding: 0; box-sizing: border-box; }
  html, body {
    width: 970px;
    height: 1200px;
    overflow: hidden;
    background: var(--label-black);
  }
  .label {
    position: relative;
    width: 970px;
    height: 1200px;
    background: var(--label-black);
  }
  .leaf-border {
    position: absolute;
    left: 0;
    top: 0;
    width: 970px;
    height: 1200px;
  }
  .brand-name {
    position: absolute;
    top: 262px;
    left: 0;
    width: 970px;
    text-align: center;
    font-family: "Great Vibes", cursive;
    font-size: 62px;
    font-weight: 400;
    color: var(--brand-bronze);
    line-height: 1;
  }
  .scent-name {
    position: absolute;
    top: 564px;
    left: 0;
    width: 970px;
    text-align: center;
    font-family: "Uncial Antiqua", serif;
    font-size: 44px;
    color: var(--text-silver);
    line-height: 1;
  }
  .product-details {
    position: absolute;
    top: 766px;
    left: 0;
    width: 970px;
    list-style: none;
    text-align: center;
    font-family: "Poppins", sans-serif;
    font-size: 30px;
    color: var(--text-silver);
    line-height: 1.2;
  }
  .product-details li { height: 76.5px; }
</style>
</head>
<body>
  <main class="label">
    <svg class="leaf-border" viewBox="0 0 970 1200" role="img" aria-label="Silver leaf-vine ornamental border framing the label">
      <defs>
        <linearGradient id="silver-band" x1="0" y1="0" x2="1" y2="1">
          <stop offset="0" stop-color="var(--silver-dark)"/>
          <stop offset="0.5" stop-color="var(--silver-mid)"/>
          <stop offset="1" stop-color="var(--silver-dark)"/>
        </linearGradient>
      </defs>
      <path fill="url(#silver-band)" fill-rule="evenodd" opacity="0.55"
            d="M92 92 H877 V1108 H92 Z M191 191 V1010 H778 V191 Z"/>
    </svg>

    <h1 class="brand-name">Fern Hollow Candle Co.</h1>
    <h2 class="scent-name">Soy Candle</h2>

    <ul class="product-details">
      <li>ALL NATURAL</li>
      <li>MADE IN USA</li>
      <li>8oz</li>
    </ul>
  </main>
</body>
</html>
```